I need a business card design for a new company that will be doing consulting work around issues of cultural competency, and diversity and inclusion. I would like the design to be crisp and clear with bold but conservative colors and incorporate shades of blue

Target Market(s)

Small businesses, schools, non-profits

Industry/Entity Type

Consulting

Font styles to use
Serif
Sans Serif

Colors
0c5ba6
6b449b
3276b5
0292cd

Requirements
Must have
• A Morrow Venture (name of company)
• Lemlem Tavish
• CEO
• lemlem@amorrowventure.com
• (215)483-2756

```html
<!DOCTYPE html>
<html lang="en">
<head>
<meta charset="utf-8">
<title>A Morrow Venture – Business Card</title>
<link href="https://fonts.googleapis.com/css2?family=Montserrat:wght@200;300;700&display=swap" rel="stylesheet">
<style>
  :root {
    --backdrop: #a3b7b5;
    --card-cyan: #0dd8f0;
    --pattern-tone: #10cfe6;
    --title-ink: #0a0f14;
    --contact-ink: #ffffff;
  }
  html, body {
    margin: 0;
    padding: 0;
    width: 1200px;
    height: 1200px;
    overflow: hidden;
    background: var(--backdrop);
  }
  .business-card {
    position: absolute;
    left: 346px;
    top: 184px;
    width: 508px;
    height: 888px;
    background: var(--card-cyan);
    overflow: hidden;
    font-family: "Montserrat", sans-serif;
  }
  .dot-pattern-area {
    position: absolute;
    inset: 0;
    background: var(--pattern-tone);
  }
  .company-name {
    position: absolute;
    left: 38px;
    top: 347px;
    margin: 0;
    font-weight: 200;
    font-size: 88px;
    line-height: 70px;
    letter-spacing: 0.5px;
    color: var(--title-ink);
    white-space: nowrap;
  }
  .contact-block {
    position: absolute;
    left: 44px;
    top: 705px;
    color: var(--contact-ink);
  }
  .contact-name {
    margin: 0;
    font-weight: 700;
    font-size: 34px;
    line-height: 34px;
  }
  .contact-line {
    margin: 0;
    font-weight: 300;
    font-size: 29px;
    line-height: 34px;
    white-space: nowrap;
  }
</style>
</head>
<body>
  <div class="business-card">
    <div class="dot-pattern-area" role="img" aria-label="Fine grid of small dark teal dots across the card"></div>
    <h1 class="company-name">A Morrow<br>Venture</h1>
    <div class="contact-block">
      <p class="contact-name">Lemlem Tavish</p>
      <p class="contact-line">CEO</p>
      <p class="contact-line">lemlem@amorrowventure.com</p>
      <p class="contact-line">(215)483-2756</p>
    </div>
  </div>
</body>
</html>
```